Business Card for Childrens Book Publisher

Would like a business card that reflects a newly established boutique childrens publishing company. The first project is a book to help raise children's self esteem titled "We Dance Till Noon." To get a better idea of the type of look I am after go to te website www.Wedancetillnoon.example.au. You can take the images from the book and use them for the business card. Would like it to have a fun innovative look and feel to it. The business is about being uplifting and positive for children, but also creating beautiful, high quality books. You can use whatever images you see on the website but I have more high res files that I can send to you over drop box or some other programs if you need them.I would like the business card to be two sided.

The information on the business card is:

Marble Lantern Books
Greta Malloway
Publisher/Author

Marble Lantern Books
marble lanterns glowing bright
T 0491 356 207
Po Box 64, Fernhill Rise, Vic 3019, Australia
ABN: 36 517 904 128
gretamalloway@marblelanternbooks.example
www.marblelanternbooks.example

Target Market(s)

Booksellers, parents, schools, kindergartens, owners of children's boutiques, retailers.

Industry/Entity Type

Boutique

Requirements
Must have
• Would it to be double sided.

```html
<!DOCTYPE html>
<html lang="en">
<head>
<meta charset="utf-8">
<title>Marble Lantern Books – Business Card</title>
<link rel="stylesheet" href="https://fonts.googleapis.com/css2?family=Noto+Serif:ital,wght@1,400;1,600;1,700&display=swap">
<style>
  :root {
    --paper: #ffffff;
    --ink: #111111;
    --grey: #6d6e71;
    --title-grey: #5a5b5e;
    --rule: #3a3a3a;
    --hair: #b8b8b8;
    --figure-top: #d9c9a8;
    --figure-mid: #f2d54a;
    --figure-low: #5a78b8;
  }
  * { margin: 0; padding: 0; box-sizing: border-box; }
  html, body {
    width: 1200px; height: 367px; overflow: hidden;
    background: var(--paper);
  }
  .sheet {
    position: relative; width: 1200px; height: 367px;
    font-family: "Noto Serif", Georgia, serif;
    font-style: italic;
  }
  .card { position: absolute; top: 0; height: 367px; width: 600px; }
  .card--front { left: 0; }
  .card--back { left: 601px; width: 599px; }
  .divider {
    position: absolute; left: 599px; top: 0; width: 2px; height: 367px;
    background: var(--rule);
  }
  .brand-title {
    position: absolute; left: 20px; top: 2px;
    font-size: 78px; font-weight: 700; line-height: 79px;
    color: var(--title-grey); letter-spacing: 1px;
    text-shadow: 4px 5px 6px rgba(0,0,0,0.28);
  }
  .brand-tagline {
    position: absolute; left: 24px; top: 258px;
    font-size: 19px; font-weight: 400; color: var(--grey);
  }
  .figure {
    position: absolute; border-radius: 40px 40px 8px 8px;
    background: linear-gradient(to bottom, var(--figure-top) 0%, var(--figure-mid) 40%, var(--figure-low) 75%, #cfe0ee 100%);
    opacity: 0.85;
  }
  .card--front .figure { left: 470px; top: 178px; width: 100px; height: 167px; }
  .card--back .figure { left: 16px; top: 205px; width: 90px; height: 145px; }
  .contact {
    position: absolute; left: 100px; width: 399px; top: 20px;
    display: flex; flex-direction: column; align-items: center;
    color: var(--grey); white-space: nowrap;
  }
  .contact__name { font-size: 27px; font-weight: 600; color: var(--ink); line-height: 34px; }
  .contact__role { font-size: 17px; font-weight: 700; line-height: 22px; }
  .contact__web { font-size: 21px; margin-top: 52px; line-height: 24px; }
  .contact__email { font-size: 17px; line-height: 24px; }
  .contact__phone { font-size: 15px; line-height: 23px; }
  .contact__rule { display: block; width: 150px; height: 1px; background: var(--hair); flex: none; }
  .contact__address { margin-top: 5px; font-size: 15px; line-height: 18.5px; text-align: center; }
  .contact__abn { margin-top: 6px; font-size: 13px; line-height: 17px; }
</style>
</head>
<body>
<main class="sheet">
  <section class="card card--front">
    <h1 class="brand-title">MARBLE<br>LANTERN<br>BOOKS</h1>
    <p class="brand-tagline">marble lanterns glowing bright</p>
    <div class="figure" role="img" aria-label="Illustration of a child with a school backpack looking upward"></div>
  </section>

  <div class="divider"></div>

  <section class="card card--back">
    <div class="figure" role="img" aria-label="Illustration of a child with a school backpack looking upward"></div>
    <div class="contact">
      <p class="contact__name">Greta Malloway</p>
      <p class="contact__role">Publisher/Author</p>
      <p class="contact__web">marblelanternbooks.example</p>
      <div class="contact__rule"></div>
      <p class="contact__email">gretamalloway@marblelanternbooks.example</p>
      <div class="contact__rule"></div>
      <p class="contact__phone">0491 356 207</p>
      <div class="contact__rule"></div>
      <p class="contact__address">Po Box 64<br>Fernhill Rise<br>Vic 3019<br>Australia</p>
      <p class="contact__abn">ABN: 36 517 904 128</p>
    </div>
  </section>
</main>
</body>
</html>
```